Consulting company with focus on aviation needs

We need a new business card design for our company. The company consults with multiple players in the industry like manufacturers and airlines. It is also a supplier and an inter-company level. Given the targeted industry (aviation) it should be both kind of serious, sound, secure, classy, ​​but also a bit technical, innovative. Should not be too playful, however, "fresh", "airy", "ligth" and "suprising" are suitabe attributes. The existing logo shall be used.

Industry/Entity Type

Airlines

```html
<!DOCTYPE html>
<html lang="en">
<head>
<meta charset="utf-8">
<title>Velaris Business Card</title>
<link rel="stylesheet" href="https://fonts.googleapis.com/css2?family=Open+Sans:wght@400;600;700&display=swap">
<style>
  :root {
    --backdrop: #3a3a3a;
    --card-paper: #ececec;
    --ink-grey: #6b6d6e;
    --ink-dark: #3f3f3f;
    --accent-orange: #f29a21;
    --accent-teal: #1aa385;
    --accent-green: #8dbb4a;
    --rule: #9a9a9a;
    --white: #ffffff;
  }
  * { box-sizing: border-box; margin: 0; padding: 0; }
  html, body {
    width: 1200px; height: 900px; overflow: hidden;
    background: var(--backdrop);
    font-family: "Open Sans", Arial, sans-serif;
  }
  .stage { position: relative; width: 1200px; height: 900px; }
  .card {
    position: absolute; top: 170px; width: 347px; height: 561px;
  }
  .card--front { left: 259px; background: var(--card-paper); text-align: center; }
  .card--back {
    left: 631px;
    background: linear-gradient(160deg, var(--accent-orange) 0%, #c9b45a 35%, #8cc05a 60%, var(--accent-teal) 100%);
  }
  .brand-dot {
    position: absolute; left: 127px; top: 72px;
    width: 92px; height: 92px; border-radius: 50%;
    background: var(--accent-teal);
  }
  .brand-name {
    position: absolute; left: 0; right: 0; top: 178px;
    font-size: 46px; font-weight: 600; letter-spacing: 10px; padding-left: 10px;
    color: var(--ink-grey); line-height: 1;
  }
  .tagline {
    position: absolute; left: 0; right: 0; top: 225px;
    font-size: 17px; color: var(--accent-orange); line-height: 1;
  }
  .person {
    position: absolute; left: 0; right: 0; top: 322px;
  }
  .person__name {
    font-size: 22px; font-weight: 700; color: var(--accent-orange);
    letter-spacing: 0.5px; line-height: 1.1;
  }
  .person__role { font-size: 15px; color: var(--ink-dark); margin-top: 1px; }
  .rule { width: 163px; height: 1px; background: var(--rule); margin: 8px auto 6px; }
  .contact { list-style: none; font-size: 15px; color: var(--ink-dark); line-height: 20px; }
  .contact__label { font-weight: 700; }
  .contact__label--phone { color: var(--accent-teal); }
  .contact__label--mobile { color: var(--accent-green); }
  .contact__label--email { color: var(--accent-orange); }
  .contact__web { font-weight: 700; color: var(--ink-grey); }
  .address { font-size: 15px; color: var(--ink-dark); line-height: 21px; }
  .back-mark {
    position: absolute; left: 0; right: 0; top: 236px;
    text-align: center; font-size: 40px; font-weight: 600;
    letter-spacing: 6px; padding-left: 6px; color: var(--white); line-height: 1;
  }
</style>
</head>
<body>
  <main class="stage">
    <section class="card card--front">
      <div class="brand-dot"></div>
      <div class="brand-name">VELARIS</div>
      <div class="tagline">Uniting Partners - Guiding Flight</div>
      <div class="person">
        <div class="person__name">MARCUS HALE</div>
        <div class="person__role">Managing Director</div>
        <div class="rule"></div>
        <ul class="contact">
          <li><span class="contact__label contact__label--phone">P:</span> 044-987 654 321</li>
          <li><span class="contact__label contact__label--mobile">M:</span> 044-987 654 321</li>
          <li><span class="contact__label contact__label--email">E:</span> info@velaris.com</li>
          <li class="contact__web">www.velaris.com</li>
        </ul>
        <div class="rule"></div>
        <p class="address">12345, Address Goes Here<br>Country Name, 123456.</p>
      </div>
    </section>
    <section class="card card--back">
      <div class="back-mark">VELARIS</div>
    </section>
  </main>
</body>
</html>
```